Gourmet food made with love and care in my country kitchen

I'd like a business card designed for my small home-based food business. I have made labelling in federation blue for my food products (Labneh cheese, spicy pumpkin chutney, dukkah, caramelised onion jam, yo-Yo biscuits, chocolate mud cake etc) and have navy and white checked surrounds/borders on my brochures so would like to stick to these country colours.
Target Market(s)
Foodies who love gourmet delicacies. Everyone who enjoys a picnic that they don't have to prepare themselves.
Industry/Entity Type
Business
Contact Information for Business Card
Brambleton Pantry
42 Tilbury Lane
Kellaby Qld 4751
Phone Jan 07 46281957 or 0412685391
Other font styles liked:
- Harrington
Look and feel

```html
<!DOCTYPE html>
<html lang="en">
<head>
<meta charset="utf-8">
<title>Brambleton Pantry – Business Card</title>
<link rel="stylesheet" href="https://fonts.googleapis.com/css2?family=Almendra&family=Open+Sans:wght@400;600&display=swap">
<style>
  :root {
    --federation-blue: #2a8fc2;
    --federation-blue-deep: #1c78aa;
    --ink-blue: #1d6c9e;
    --bullet-blue: #2680b3;
    --panel-light: #ececec;
    --panel-shade: #d9d9d9;
    --band-light: #c6c8cb;
    --band-shade: #b3b5b8;
    --photo-field: #6e9a58;
    --photo-sky: #b9d2e4;
    --photo-table: #5b4a3c;
    --photo-pastry: #d9a860;
  }
  html, body {
    margin: 0;
    padding: 0;
    overflow: hidden;
    background: #ffffff;
  }
  .card {
    position: relative;
    width: 1200px;
    height: 741px;
    overflow: hidden;
    background: linear-gradient(180deg, var(--federation-blue) 0%, var(--federation-blue-deep) 100%);
    font-family: 'Open Sans', Arial, sans-serif;
  }
  .info-panel {
    position: absolute;
    left: 0;
    top: 93px;
    width: 872px;
    height: 431px;
    border-radius: 0 12px 12px 0;
    background: linear-gradient(180deg, var(--panel-light) 0%, var(--panel-shade) 100%);
    box-shadow: 2px 4px 10px rgba(0, 0, 0, 0.35);
  }
  .business-name {
    position: absolute;
    left: 41px;
    top: 90px;
    width: 808px;
    margin: 0;
    font-family: 'Almendra', 'Times New Roman', serif;
    font-weight: 400;
    font-size: 94px;
    line-height: 1;
    letter-spacing: 2px;
    color: var(--ink-blue);
    white-space: nowrap;
  }
  .offerings {
    position: absolute;
    left: 92px;
    top: 204px;
    margin: 0;
    padding: 0;
    list-style: none;
    font-family: 'Almendra', 'Times New Roman', serif;
    font-size: 32px;
    line-height: 41px;
    letter-spacing: 2px;
    color: var(--bullet-blue);
  }
  .offerings li::before {
    content: "•";
    margin-right: 12px;
  }
  .address {
    position: absolute;
    left: 62px;
    top: 342px;
    margin: 0;
    font-size: 28px;
    line-height: 1;
    color: var(--ink-blue);
    white-space: nowrap;
  }
  .contact {
    position: absolute;
    left: 229px;
    top: 395px;
    margin: 0;
    font-style: normal;
    color: var(--ink-blue);
    line-height: 1;
  }
  .contact p { margin: 0; white-space: nowrap; }
  .contact .email { font-size: 22px; }
  .contact .phone { font-size: 20px; margin-top: 18px; }
  .contact .social { font-size: 22px; margin-top: 14px; letter-spacing: 1px; }
  .photo {
    position: absolute;
  }
  .photo-farm {
    left: 46px;
    top: 379px;
    width: 170px;
    height: 145px;
    background: linear-gradient(180deg, var(--photo-sky) 0%, #9fbf9a 45%, var(--photo-field) 100%);
  }
  .photo-galette {
    left: 644px;
    top: 212px;
    width: 207px;
    height: 170px;
    background: radial-gradient(ellipse at 50% 62%, var(--photo-pastry) 0%, #8c6a48 45%, var(--photo-table) 100%);
  }
  .tagline-band {
    position: absolute;
    left: 0;
    top: 600px;
    width: 1200px;
    height: 97px;
    background: linear-gradient(180deg, var(--band-light) 0%, var(--band-shade) 100%);
  }
  .tagline {
    position: absolute;
    left: 128px;
    top: 614px;
    margin: 0;
    font-family: 'Almendra', 'Times New Roman', serif;
    font-size: 23px;
    line-height: 29px;
    letter-spacing: 4.2px;
    color: var(--federation-blue);
    white-space: nowrap;
  }
</style>
</head>
<body>
  <div class="card">
    <div class="info-panel"></div>

    <h1 class="business-name">Brambleton Pantry</h1>

    <ul class="offerings">
      <li>Gourmet market food</li>
      <li>Vintage Picnic Hampers</li>
      <li>Cooking Classes</li>
    </ul>

    <p class="address">42 Tilbury Lane, Hollis Vale Via Kellaby</p>

    <div class="photo photo-farm" role="img" aria-label="Country farm scene with gum trees, white fence and green cane fields"></div>
    <div class="photo photo-galette" role="img" aria-label="Rustic tomato galette on a dark plate on a verandah table with a bottle of oil"></div>

    <address class="contact">
      <p class="email">Email: hello@brambletonpantry.com.au</p>
      <p class="phone">Phone Jan: 07 46281957 or 0412685391</p>
      <p class="social">Socials: Brambleton Pantry</p>
    </address>

    <div class="tagline-band"></div>
    <p class="tagline">Gourmet food made in my country kitchen, using fresh<br>ingredients,for your enjoyment and convenience. Jan Marlow</p>
  </div>
</body>
</html>
```